Van sign writing design( calling the best of the best designers)

Hi Guys
Im after a one of a kind wow statement design to print onto my van.I have just started a plumbing a gasfitting company so i want to show case the type of work i can complete.

The plumbing van attached is the exact wow design im after.

The start of the side of the van in orange merging into the blue color
So in the back ground of the orange colour to have flames and with the blue colour to have a realistic water flowing or splash image as attached

Turn my logo into a translucent/ back ground image as shown in the attachment instead of the orange and blue.

Contact number down the bottom between the front and rear wheels 0219384752
Quendo/lumo brightpurse images as i carry a mobile machine and pinglodge.

Target Market(s)

everyone driving by

Colors
0555a3
f37122

Requirements
Must have
• My logo and stated info
Nice to have
• as stated

```html
<!DOCTYPE html>
<html lang="en">
<head>
<meta charset="utf-8">
<title>Tapline Plumber &amp; Gas — Van Side Wrap</title>
<link rel="stylesheet" href="https://fonts.googleapis.com/css2?family=Montserrat:ital,wght@0,700;0,800;1,700&display=swap">
<style>
  :root {
    --brand-blue: #0555a3;
    --brand-orange: #f37122;
    --navy: #0b1a4d;
    --deep-navy: #070f33;
    --white: #ffffff;
    --page: #eef0f3;
    --silver: #c9ccd1;
    --burner-blue: #1f5fd8;
  }
  * { margin: 0; padding: 0; box-sizing: border-box; }
  html, body { width: 1200px; height: 900px; overflow: hidden; background: var(--page); }
  body { font-family: "Montserrat", Arial, sans-serif; color: var(--white); }

  .canvas { position: relative; width: 1200px; height: 900px; }

  .wrap-panel {
    position: absolute; left: 40px; top: 210px; width: 1120px; height: 480px;
    border-radius: 60px 28px 28px 40px; overflow: hidden;
    background: linear-gradient(90deg, var(--brand-orange) 0%, var(--brand-orange) 14%, var(--brand-blue) 36%, var(--brand-blue) 62%, var(--navy) 82%, var(--deep-navy) 100%);
  }

  .flame-backdrop {
    position: absolute; left: 428px; top: 0; width: 330px; height: 186px;
    background: linear-gradient(90deg, var(--brand-orange), rgba(5,85,163,0.35));
    opacity: .85;
  }
  .water-backdrop {
    position: absolute; left: 440px; top: 186px; width: 330px; height: 200px;
    background: radial-gradient(ellipse at 40% 50%, rgba(255,255,255,.16), rgba(5,85,163,0) 70%);
  }

  .contact { position: absolute; left: 58px; top: 228px; width: 180px; text-align: center; }
  .contact .phone {
    font-size: 35px; font-weight: 800; line-height: 1.1; letter-spacing: -.5px;
    color: var(--white); -webkit-text-stroke: 3px var(--brand-blue); paint-order: stroke fill;
  }
  .social { margin-top: 26px; display: flex; flex-direction: column; align-items: center; gap: 6px; }
  .social .dot { width: 30px; height: 30px; border-radius: 50%; background: var(--brand-blue); }
  .social .label { font-size: 14px; font-weight: 700; line-height: 1.2; }

  .logo-mark {
    position: absolute; left: 256px; top: 30px; width: 280px; height: 420px;
    display: flex; flex-direction: column; align-items: center; justify-content: center; gap: 18px;
  }
  .logo-mark .disc {
    width: 200px; height: 200px; border-radius: 50%;
    background: var(--brand-orange); border: 10px solid var(--silver);
  }
  .logo-mark .name { font-size: 26px; font-weight: 800; color: var(--white); white-space: nowrap; }

  .headline {
    position: absolute; right: 84px; top: 34px; text-align: right;
    font-weight: 800; line-height: 1; letter-spacing: -1px; white-space: nowrap;
  }
  .headline .main { display: block; font-size: 54px; color: var(--white); }
  .headline .sub { display: block; font-size: 54px; color: var(--brand-orange); padding-right: 176px; margin-top: 6px; }

  .services {
    position: absolute; left: 548px; top: 212px; list-style: none;
    font-size: 21px; font-weight: 700; line-height: 32px; white-space: nowrap;
  }
  .services li::before { content: "• "; font-size: 14px; vertical-align: middle; }

  .burner-photo {
    position: absolute; left: 800px; top: 180px; width: 312px; height: 196px; border-radius: 40px;
    background: radial-gradient(ellipse at center, var(--burner-blue) 0%, var(--brand-blue) 45%, rgba(7,15,51,0) 80%);
  }

  .web-band {
    position: absolute; left: 440px; top: 397px; width: 332px; height: 46px;
    background: linear-gradient(90deg, var(--brand-blue) 0%, var(--brand-orange) 22%, var(--brand-orange) 100%);
    display: flex; align-items: center; justify-content: flex-end; padding-right: 20px;
  }
  .web-band .url { font-size: 21px; font-weight: 700; font-style: italic; color: var(--white); white-space: nowrap; }
</style>
</head>
<body>
<main class="canvas">
  <section class="wrap-panel" aria-label="Van side wrap artwork">
    <div class="flame-backdrop" role="img" aria-label="Backdrop photograph of orange flames"></div>
    <div class="water-backdrop" role="img" aria-label="Backdrop photograph of splashing water"></div>

    <div class="contact">
      <p class="phone">+64 21<br>938 4752</p>
      <div class="social">
        <span class="dot"></span>
        <span class="label">Find us on<br>pinglodge</span>
      </div>
    </div>

    <div class="logo-mark">
      <span class="disc"></span>
      <span class="name">Tapline Plumber</span>
    </div>

    <h1 class="headline">
      <span class="main">TAPLINE PLUMBER</span>
      <span class="sub">&amp; GAS</span>
    </h1>

    <div class="burner-photo" role="img" aria-label="Photograph of a gas stove burner with blue flames"></div>

    <ul class="services">
      <li>Plumbing &amp; Gas</li>
      <li>Installations</li>
      <li>Repairs Servicing</li>
      <li>Gas Hot Water Pipe</li>
      <li>Rack to be wrapped</li>
    </ul>

    <div class="web-band"><span class="url">www.taplineplumber</span></div>
  </section>
</main>
</body>
</html>
```